Quillon’s Prime Response Vehicle Branding

I am looking to get a half wrap for vehicles to assist in branding for a fire water storm and mold restoration company. I would like to have something similar to the photo loaded to include RWTB Certified Firm Logo and we also use Vans and Trucks...

Target Market(s)

Insurance claims damage from fire water floods and storms and mold....

Requirements
Must have
• The listed logo that I have uploaded. I would also like to have the fact of services provided (see below of services provided)
I would like something for the back of trucks / vans also to be included.

Please list where it looks uniform the following:
- Property Damage Restoration Specialist.
- 24 hr Emergency Service
- Web site: Quillonprimeresponse.com
- Office line: 904-618-3927

Services Provided to list:
Fire - Water - Mold - Storm
Restoration
Nice to have
• I would like to have some designs that incorporate in the background showing fire, wind / water / possibly if that can fit into what you design and it does not need to overwhelm the design though...
Should not have
• I do not want the logo changed.
I do not want it to be to busy.

```html
<!DOCTYPE html>
<html lang="en">
<head>
<meta charset="utf-8">
<title>Quillon Prime Response – Vehicle Wrap</title>
<link href="https://fonts.googleapis.com/css2?family=Roboto+Condensed:ital,wght@0,400;0,700;1,700&display=swap" rel="stylesheet">
<style>
  :root {
    --bg-top: #060606;
    --bg-bottom: #4d474c;
    --brand-red: #a50f15;
    --ink: #111111;
    --body-white: #f4f4f4;
    --photo-light: #cfcfcf;
    --photo-dark: #3a3a3a;
    --text-white: #ffffff;
  }
  * { margin: 0; padding: 0; box-sizing: border-box; }
  html, body { width: 1200px; height: 1154px; overflow: hidden; }
  body {
    background: linear-gradient(180deg, var(--bg-top) 0%, var(--bg-bottom) 100%);
    font-family: "Roboto Condensed", "Arial Narrow", sans-serif;
    position: relative;
  }
  .brand-lockup {
    position: absolute; left: 42px; top: 58px;
    display: flex; align-items: center; gap: 18px;
  }
  .brand-square { width: 62px; height: 62px; background: var(--brand-red); }
  .brand-name { color: var(--text-white); font-weight: 700; font-size: 46px; line-height: 1; }
  .wrap-panel { position: absolute; left: 80px; width: 1040px; height: 250px; }
  .wrap-panel--driver { top: 340px; }
  .wrap-panel--passenger { top: 770px; }
  .wrap-panel svg { display: block; width: 100%; height: 100%; }
  .t-phone { font-weight: 700; font-size: 26px; fill: var(--brand-red); }
  .t-name { font-weight: 700; font-size: 32px; fill: var(--ink); }
  .t-hours { font-weight: 700; font-style: italic; font-size: 28px; fill: var(--ink); }
  .t-hours-tag { font-weight: 700; font-size: 6.5px; fill: var(--text-white); }
  .t-web { font-size: 15px; fill: var(--brand-red); }
  .t-band { font-size: 14px; fill: var(--text-white); letter-spacing: 0.2px; }
  .t-service { font-weight: 700; font-size: 14px; fill: var(--brand-red); stroke: var(--text-white); stroke-width: 2.5px; paint-order: stroke; }
</style>
</head>
<body>

<div class="brand-lockup">
  <div class="brand-square"></div>
  <div class="brand-name">Quillon Prime Response</div>
</div>

<!-- Driver side: cab on the left, bed on the right -->
<section class="wrap-panel wrap-panel--driver" aria-label="Driver side wrap layout">
  <svg viewBox="0 0 1040 250" xmlns="http://www.w3.org/2000/svg">
    <defs>
      <linearGradient id="photoToneA" x1="0" y1="0" x2="1" y2="1">
        <stop offset="0" stop-color="var(--photo-dark)"/>
        <stop offset="0.55" stop-color="var(--photo-light)"/>
        <stop offset="1" stop-color="var(--photo-dark)"/>
      </linearGradient>
    </defs>
    <rect class="body-side" x="0" y="0" width="1040" height="240" rx="18" fill="var(--body-white)"/>
    <rect class="band-red" x="300" y="204" width="460" height="28" fill="var(--brand-red)"/>
    <path class="photo-strip" role="img" aria-label="Black and white photos of fire crews, water damage, mold cleanup and storm repair"
          d="M818,4 L1040,4 L1040,240 L690,240 C760,205 790,120 818,4 Z" fill="url(#photoToneA)"/>
    <g class="service-dividers" stroke-width="4">
      <line x1="870" y1="4" x2="820" y2="240" stroke="var(--text-white)"/>
      <line x1="874" y1="4" x2="824" y2="240" stroke="var(--brand-red)" stroke-width="2"/>
      <line x1="926" y1="4" x2="876" y2="240" stroke="var(--text-white)"/>
      <line x1="930" y1="4" x2="880" y2="240" stroke="var(--brand-red)" stroke-width="2"/>
      <line x1="980" y1="4" x2="930" y2="240" stroke="var(--text-white)"/>
      <line x1="984" y1="4" x2="934" y2="240" stroke="var(--brand-red)" stroke-width="2"/>
    </g>
    <path class="swoosh" d="M788,4 L814,4 C786,132 758,200 690,206 L330,206 L330,196 L680,193 C740,182 764,120 788,4 Z" fill="var(--ink)"/>
    <rect x="290" y="191" width="40" height="5" fill="var(--ink)"/>

    <text class="t-service" x="826" y="24">Fire</text>
    <text class="t-service" x="880" y="24">Water</text>
    <text class="t-service" x="936" y="24">Mold</text>
    <text class="t-service" x="988" y="24">Storm</text>

    <text class="t-phone" x="100" y="72">904-618-3927</text>
    <rect x="330" y="52" width="64" height="64" fill="var(--brand-red)"/>
    <text class="t-name" x="408" y="100">Quillon Prime Response</text>

    <text class="t-hours" x="316" y="184">24HR</text>
    <rect x="306" y="190" width="74" height="10" fill="var(--ink)"/>
    <text class="t-hours-tag" x="343" y="197.5" text-anchor="middle">EMERGENCY SERVICE</text>
    <text class="t-web" x="545" y="188" text-anchor="middle">www.<tspan font-weight="700">QuillonPrimeResponse</tspan>.com</text>
    <text class="t-band" x="530" y="223" text-anchor="middle">PROPERTY DAMAGE RESTORATION SPECIALIST</text>
  </svg>
</section>

<!-- Passenger side: bed on the left, cab on the right -->
<section class="wrap-panel wrap-panel--passenger" aria-label="Passenger side wrap layout">
  <svg viewBox="0 0 1040 250" xmlns="http://www.w3.org/2000/svg">
    <defs>
      <linearGradient id="photoToneB" x1="1" y1="0" x2="0" y2="1">
        <stop offset="0" stop-color="var(--photo-dark)"/>
        <stop offset="0.55" stop-color="var(--photo-light)"/>
        <stop offset="1" stop-color="var(--photo-dark)"/>
      </linearGradient>
    </defs>
    <rect class="body-side" x="0" y="0" width="1040" height="240" rx="18" fill="var(--body-white)"/>
    <g transform="translate(1040,0) scale(-1,1)">
      <rect class="band-red" x="200" y="204" width="560" height="28" fill="var(--brand-red)"/>
      <path class="photo-strip" role="img" aria-label="Black and white photos of fire crews, water damage, mold cleanup and storm repair"
            d="M818,4 L1040,4 L1040,240 L690,240 C760,205 790,120 818,4 Z" fill="url(#photoToneB)"/>
      <g class="service-dividers" stroke-width="4">
        <line x1="870" y1="4" x2="820" y2="240" stroke="var(--text-white)"/>
        <line x1="874" y1="4" x2="824" y2="240" stroke="var(--brand-red)" stroke-width="2"/>
        <line x1="926" y1="4" x2="876" y2="240" stroke="var(--text-white)"/>
        <line x1="930" y1="4" x2="880" y2="240" stroke="var(--brand-red)" stroke-width="2"/>
        <line x1="980" y1="4" x2="930" y2="240" stroke="var(--text-white)"/>
        <line x1="984" y1="4" x2="934" y2="240" stroke="var(--brand-red)" stroke-width="2"/>
      </g>
      <path class="swoosh" d="M788,4 L814,4 C786,132 758,200 690,206 L330,206 L330,196 L680,193 C740,182 764,120 788,4 Z" fill="var(--ink)"/>
      <rect x="230" y="191" width="100" height="5" fill="var(--ink)"/>
    </g>

    <text class="t-service" x="12" y="24">Fire</text>
    <text class="t-service" x="68" y="24">Water</text>
    <text class="t-service" x="124" y="24">Mold</text>
    <text class="t-service" x="178" y="24">Storm</text>

    <text class="t-phone" x="990" y="72" text-anchor="end">904-618-3927</text>
    <rect x="380" y="52" width="64" height="64" fill="var(--brand-red)"/>
    <text class="t-name" x="458" y="100">Quillon Prime Response</text>

    <text class="t-web" x="560" y="188" text-anchor="middle">www.<tspan font-weight="700">QuillonPrimeResponse</tspan>.com</text>
    <text class="t-hours" x="728" y="184">24HR</text>
    <rect x="718" y="190" width="74" height="10" fill="var(--ink)"/>
    <text class="t-hours-tag" x="755" y="197.5" text-anchor="middle">EMERGENCY SERVICE</text>
    <text class="t-band" x="540" y="223" text-anchor="middle">PROPERTY DAMAGE RESTORATION SPECIALIST</text>
  </svg>
</section>

</body>
</html>
```